Corporate Breakfast Flyer - Breakfast Talk (One Page)

Create a flyer with below using your own selection of content and images from the below. You do not have to use all images I have left them all there for your choice. Please use blue type colors like in our logo. Should be a corporate and professional feel to it.

Venue: Brindlemere Links Club 17 Carrowvale St, Fernleigh NSW 2190
Date: Thursday the 22nd of September 2016
7.30am: Breakfast and networking
8.00am: Dylan Morrow speaking – Leadership and Motivation
9.00am: Business Card draw and finish

• Mini croissants on arrival – Ham & cheese, tomato & cheese, plain
• Toast station – assorted sliced breads & spreads
• Banana bread slice with honey ricotta
• Chicken & herb chipolata
• Marinated lamb chops
• Creamy scrambled eggs with chives
• Mushroom & cherry tomato kebabs
• Hash browns
• Assorted fruit cocktails with yoghurt & granola, juice station
• Tea and coffee station included
Topic: Leadership and Motivation
Speaker profile (Dylan Morrow):
Dylan Morrow is a four-time Meridian Cup competitor, winning basketball player, coach, entrepreneur, motivational speaker, brand ambassador - and one of Australia's most recognized personalities and sporting figures.
He was the first-ever Australian player to be signed to the PCX from the QVR and he also captained the Harbour Falcons to their first-ever title, helping to raise the profile of basketball around Australia. He has represented Australia at four Meridian Cup and played professionally for more than 20 years in Australia, Europe and the PCX. In February 2012 he was appointed Head Coach of the Harbour Falcons.
Following his retirement from playing, Dylan earned a reputation as a successful entrepreneur and businessman. He built up a successful business in fast food franchising with more than 30 stores across six different brands which, at its peak in 2010, employed over 350 people. After his company was severely affected by the collapse of an KTE listed company in which he had purchased a 10-year contract, Dylan had to start all over again.
Dylan has also held hosting, commentary and columnist roles with WMR, Vista Seven, Orbit Broadcast and Pike Athletics.

Target Market(s)

Finance leaders, Finance Directors, Controllers and CFO's

Font styles to use
Serif
Sans Serif

Colors
33a6d7
0592cd
0355a3
3276b5
85abd2
85cae6

Requirements
Must have
• Must be one page A4 will be sent electronically
Nice to have
• Any other images you feel may be pertinant, I have attached lots of images for you to use for this project please do not use to many. I have attached more so you have more selection
Should not have
• All Images

```html
<!DOCTYPE html>
<html lang="en">
<head>
<meta charset="utf-8">
<title>Breakfast Talk – Leadership and Motivation</title>
<link href="https://fonts.googleapis.com/css2?family=Open+Sans:wght@400;600;700;800&family=PT+Sans:wght@400;700&display=swap" rel="stylesheet">
<style>
:root{
  --grey-top:#d9dadc;
  --grey-mid:#cfd1d4;
  --ink:#1d1d1f;
  --blue-deep:#0355a3;
  --blue-mid:#3276b5;
  --blue-bright:#0592cd;
  --blue-sky:#33a6d7;
  --blue-soft:#85cae6;
  --blue-pale:#85abd2;
  --white:#ffffff;
  --logo-dark:#2b2b2b;
}
*{margin:0;padding:0;box-sizing:border-box}
html,body{width:927px;height:1200px;overflow:hidden;background:var(--white)}
.flyer{position:relative;width:927px;height:1200px;overflow:hidden;background:var(--grey-mid);font-family:"PT Sans",Arial,sans-serif}
.masthead{position:absolute;left:0;top:0;width:927px;height:165px;background:linear-gradient(#e2e3e5,var(--grey-top))}
.brand{position:absolute;left:84px;top:48px;display:flex;align-items:center;gap:14px}
.brand-dot{width:56px;height:56px;border-radius:50%;background:var(--blue-bright)}
.brand-name{font-family:"Open Sans",Arial,sans-serif;font-weight:600;font-size:40px;color:#4a4a4c;letter-spacing:-.5px}
.venue-mark{position:absolute;left:700px;top:28px;width:158px;height:118px;background:var(--logo-dark);display:flex;align-items:center;justify-content:center;text-align:center;padding:10px}
.venue-mark span{font-family:"PT Sans",serif;font-size:15px;color:#e9e4d8;line-height:1.2;letter-spacing:.5px}
.title-band{position:absolute;left:0;top:165px;width:927px;height:156px;background:linear-gradient(90deg,#2f87c8,#3d9ad6 50%,#5aaee0);border-top:3px solid var(--blue-mid)}
.title-band h1{position:absolute;left:68px;top:10px;font-family:"Open Sans",Verdana,sans-serif;font-weight:800;font-size:50px;color:var(--ink);letter-spacing:-.5px}
.event-date{position:absolute;left:0;width:927px;top:72px;text-align:center;font-family:"Open Sans",sans-serif;font-size:28px;color:var(--white)}
.event-venue{position:absolute;left:0;width:927px;top:116px;text-align:center;font-family:"Open Sans",sans-serif;font-size:17px;color:var(--white)}
.schedule{position:absolute;left:68px;top:352px;list-style:none;font-family:"Open Sans",Verdana,sans-serif;font-weight:700;font-size:19px;color:var(--ink);line-height:27px}
.schedule li{display:flex}
.schedule .time{width:106px;flex:none}
.topic{position:absolute;left:62px;top:505px;font-family:"Open Sans",Verdana,sans-serif;font-weight:700;font-size:50px;line-height:64px;color:var(--blue-bright)}
.wave{position:absolute;left:0;top:620px;width:927px;height:120px}
.food-photo{position:absolute;left:537px;top:321px;width:390px;height:395px;background:linear-gradient(160deg,#c7dff2,#a9cdea 55%,#e9d9c3)}
.menu{position:absolute;left:568px;top:333px;list-style:none;font-family:"PT Sans",Arial,sans-serif;font-size:13.5px;line-height:20.8px;color:var(--ink);width:340px}
.menu li{padding-left:10px;position:relative}
.menu li::before{content:"";position:absolute;left:0;top:8px;width:5px;height:5px;border-radius:50%;background:var(--ink)}
.speaker-area{position:absolute;left:0;top:720px;width:927px;height:376px;background:linear-gradient(90deg,#1f6fb6,#2c86cc 55%,#2f8fd2)}
.speaker-photo{position:absolute;left:57px;top:20px;width:243px;height:246px;background:linear-gradient(#4a4d55,#6d6f75)}
.speaker-bio{position:absolute;left:326px;top:18px;width:592px;color:var(--white)}
.speaker-bio h2{font-family:"Open Sans",Arial,sans-serif;font-weight:700;font-size:19px;margin-bottom:4px}
.speaker-bio p{font-family:"PT Sans",Arial,sans-serif;font-size:14.2px;line-height:20.6px}
.contact{position:absolute;left:0;top:1095px;width:927px;height:105px;background:linear-gradient(90deg,#4aa8dc,#2f8fd2 50%,#3a98d6);border-top:2px solid var(--blue-soft);text-align:center;color:var(--white);font-family:"Open Sans",Arial,sans-serif}
.phone{position:absolute;left:0;width:927px;top:28px;font-size:24px;display:flex;justify-content:center;align-items:center;gap:8px}
.web{position:absolute;left:0;width:927px;top:56px;font-size:23px}
</style>
</head>
<body>
<main class="flyer">
  <header class="masthead">
    <div class="brand"><span class="brand-dot"></span><span class="brand-name">Calder Pryce</span></div>
    <div class="venue-mark"><span>Brindlemere Links Club</span></div>
  </header>

  <section class="title-band">
    <h1>Breakfast Talk</h1>
    <p class="event-date">Thursday | September 22, 2016</p>
    <p class="event-venue">Brindlemere Links Club, 17 Carrowvale St, Fernleigh NSW 2190</p>
  </section>

  <ul class="schedule">
    <li><span class="time">7:30 AM:</span><span>Breakfast and Networking</span></li>
    <li><span class="time">8:00 AM:</span><span>Dylan Morrow Speaking on<br>Leadership Motivation</span></li>
    <li><span class="time">9:00 AM:</span><span>Business Card Draw and Finish</span></li>
  </ul>

  <h2 class="topic">Leadership and<br>Motivation</h2>

  <svg class="wave" viewBox="0 0 927 120" preserveAspectRatio="none" aria-hidden="true">
    <path d="M0 30 C300 95 620 110 927 70 L927 120 L0 120 Z" fill="#1f6fb6"/>
    <path d="M0 30 C300 95 620 110 927 70" fill="none" stroke="#85cae6" stroke-width="2" opacity=".6"/>
  </svg>

  <div class="food-photo" role="img" aria-label="Breakfast table with croissants, orange juice, coffee, strawberries and jam"></div>
  <ul class="menu">
    <li>Mini croissants on arrival<br>(ham &amp; cheese, tomato &amp; cheese, plain)</li>
    <li>Toast Station (Assorted sliced breads &amp; spreads)</li>
    <li>Banana Bread slice with honey ricotta</li>
    <li>Chicken &amp; herb chipolata</li>
    <li>Marinated Lamb Chops</li>
    <li>Creamy Scrambled Eggs with chives</li>
    <li>Mushroom &amp; Cherry tomato kebabs</li>
    <li>Hash browns</li>
    <li>Assorted fruit cocktails with yoghurt<br>and granola, juice station</li>
    <li>Tea and Coffee Station included</li>
  </ul>

  <section class="speaker-area">
    <div class="speaker-photo" role="img" aria-label="Portrait photo of speaker Dylan Morrow"></div>
    <div class="speaker-bio">
      <h2>Dylan Morrow</h2>
      <p>DYLAN MORROW is a four-time Meridian Cup competitor, winning basketball player, coach, entrepreneur, motivational speaker, brand ambassador - and one of Australia's most recognized personalities and sporting figure.</p>
      <p>He was the first-ever Australian player to be signed to the PCX from the QVR and he also captained the Harbour Falcons to their first-ever title, helping to raise the profile of basketball around Australia. He has represented Australia at four Meridian Cup played professionally for more than 20 years in Australia, Europe and the PCX. In February 2012 he was appointed head coach of the Harbour Falcons.</p>
      <p>Following his retirement from playing, Dylan earned a reputation as a successful entrepreneur and businessman. He built up a successful business in fast food franchising with more than 30 stores across six different brands which, at its peak in 2010, employed over 350 people. After his company was severely affected by the collapse of an KTE listed company in which he had purchased a 10-year contract, Dylan had to start all over again.</p>
      <p>Dylan has also been hosting commentary and columnist roles with WMR, Vista Seven, Orbit Broadcast and Pike Athletics.</p>
    </div>
  </section>

  <footer class="contact">
    <p class="phone">
      <svg width="22" height="22" viewBox="0 0 24 24" aria-hidden="true"><circle cx="12" cy="12" r="10.5" fill="none" stroke="#fff" stroke-width="1.5"/><path d="M8.5 6.5c.6-.4 1.2-.3 1.5.3l1 2c.2.5 0 1-.4 1.3l-.7.5c.6 1.5 1.6 2.6 3 3.3l.6-.7c.3-.4.9-.5 1.3-.3l2 1c.6.3.7 1 .3 1.5-.9 1.2-2 1.6-3.4 1-2.8-1.2-4.8-3.4-5.8-6.2-.4-1.2 0-2.2.6-2.7z" fill="#fff"/></svg>
      +61 02 5550 1948
    </p>
    <p class="web">www.calderpryce.com.au</p>
  </footer>
</main>
</body>
</html>
```